Velmora Business Card

We need a design for business cards for our new company. We are a resident safety and security company company that focuses on senior living communities. we provide Nurse call, Access control, CCTV, Wired and wireless network infrastructure, Wander Management, and much more!

Our logo is the circuit board shield. Representing our high tech security solutions. I would like the business card to bring the same theme with perhaps some circuit board traces around the card similar to our logo

```html
<!DOCTYPE html>
<html lang="en">
<head>
<meta charset="utf-8">
<title>Velmora Business Card</title>
<link rel="stylesheet" href="https://fonts.googleapis.com/css2?family=Arimo:wght@400;700&display=swap">
<style>
  :root {
    --backdrop: #e6e6e4;
    --card: #2d2d2e;
    --card-deep: #1c1c1d;
    --edge: #0a6fd6;
    --accent: #1a73e8;
    --accent-light: #1fa3f0;
    --ink: #f2f2f2;
    --emboss: #8d8d90;
  }
  * { margin: 0; padding: 0; box-sizing: border-box; }
  html, body { width: 1200px; height: 801px; overflow: hidden; background: var(--backdrop); }
  body { position: relative; font-family: "Arimo", Arial, sans-serif; }

  .card {
    position: absolute;
    width: 540px;
    height: 309px;
    background: var(--card);
    border-bottom: 4px solid var(--edge);
    overflow: hidden;
    box-shadow: 0 14px 30px rgba(0,0,0,.28);
  }
  .card--front { left: 40px; top: 246px; }
  .card--back { left: 620px; top: 246px; }

  .shield-area {
    position: absolute;
    right: -70px;
    top: -60px;
    width: 330px;
    height: 330px;
    border-radius: 50%;
    background: radial-gradient(circle at 70% 30%, #a6a6a8 0%, #5a5a5c 45%, var(--card-deep) 100%);
  }

  .wordmark {
    position: absolute;
    left: 34px;
    top: 40px;
    font-size: 34px;
    font-weight: 400;
    letter-spacing: 3px;
    color: var(--accent);
    text-transform: uppercase;
  }

  .person { position: absolute; left: 34px; top: 110px; }
  .person__name {
    font-size: 22px;
    font-weight: 700;
    color: var(--accent-light);
    text-transform: uppercase;
    letter-spacing: .5px;
  }
  .person__title { font-size: 17px; color: var(--ink); margin-top: 3px; }

  .contact { position: absolute; left: 34px; top: 186px; list-style: none; }
  .contact__item {
    display: flex;
    align-items: center;
    gap: 8px;
    font-size: 16px;
    line-height: 24px;
    color: var(--ink);
  }
  .contact__icon { width: 13px; height: 13px; flex: none; }

  .tab {
    position: absolute;
    left: 0;
    bottom: 36px;
    width: 8px;
    height: 30px;
    border-radius: 0 4px 4px 0;
    background: var(--accent-light);
  }

  .brand {
    position: absolute;
    left: 0;
    right: 0;
    top: 70px;
    display: flex;
    flex-direction: column;
    align-items: center;
    gap: 18px;
  }
  .brand__mark {
    width: 110px;
    height: 110px;
    border-radius: 50%;
    background: #3a3a3c;
  }
  .brand__name {
    font-size: 40px;
    font-weight: 400;
    letter-spacing: 6px;
    color: var(--emboss);
    text-transform: uppercase;
  }
</style>
</head>
<body>
  <section class="card card--front" aria-label="Card front">
    <div class="shield-area" role="img" aria-label="Company emblem area"></div>
    <div class="wordmark">Velmora</div>
    <div class="person">
      <div class="person__name">Marcus Ellery</div>
      <div class="person__title">President</div>
    </div>
    <ul class="contact">
      <li class="contact__item">
        <svg class="contact__icon" viewBox="0 0 16 16"><path fill="#1fa3f0" d="M3 1l3 3-2 2c1 2 3 4 5 5l2-2 3 3-2 3C6 15 1 10 1 3z"/></svg>
        (555) 014-2290
      </li>
      <li class="contact__item">
        <svg class="contact__icon" viewBox="0 0 16 16"><rect x="4" y="1" width="8" height="14" rx="1.5" fill="none" stroke="#1fa3f0" stroke-width="1.6"/></svg>
        (555) 014-7731
      </li>
      <li class="contact__item">
        <svg class="contact__icon" viewBox="0 0 16 16"><rect x="1" y="3" width="14" height="10" rx="1" fill="#1fa3f0"/><path d="M1 4l7 5 7-5" fill="none" stroke="#2d2d2e" stroke-width="1.4"/></svg>
        Marcus@Velmora.com
      </li>
      <li class="contact__item">
        <svg class="contact__icon" viewBox="0 0 16 16"><circle cx="8" cy="8" r="7" fill="#1fa3f0"/><path d="M1 8h14M8 1c-3 4-3 10 0 14M8 1c3 4 3 10 0 14" fill="none" stroke="#2d2d2e" stroke-width="1"/></svg>
        www.Velmora.com
      </li>
    </ul>
    <div class="tab"></div>
  </section>

  <section class="card card--back" aria-label="Card back">
    <div class="brand">
      <div class="brand__mark"></div>
      <div class="brand__name">Velmora</div>
    </div>
  </section>
</body>
</html>
```